Kitchen manufaturer business card/logo design

I am a small kitchen manufacturing company that makes and installs all sorts of cabinetry.

The colours im looking to incorporate in the card are light/baby blue, white and black.

Incorporate 5 stars to show quality workmanship and product.

Looking for a modern classy design.
Updates

Hey guys, New idea. The logo should be made using HK in the most modern way possible as well as the full company name below it. Thanks.

Target Market(s)

Anyone with a home thats looking for a new cabinetry of any sort.

Industry/Entity Type

Business

Contact Information for Business Card

Harbor Kitchens
Ted Lowther
PH 0491 358 902
Email- harborkitchens@mailvane.example
ABN- 83 507 962 318
-Kitchens
-Vanities
-Laundries
-Media Units
-Studies
-Wardrobes
-3D Computer Designs

Requirements
Must have

• The front of the card must only have the company name.
The different types of cabinetry I do must be on the back of the card in point form but instead of using points use stars.
Nice to have
• Just think classy and quality

```html
<!DOCTYPE html>
<html lang="en">
<head>
<meta charset="utf-8">
<title>Harbor Kitchens – Business Card</title>
<link rel="stylesheet" href="https://fonts.googleapis.com/css2?family=Bebas+Neue&family=Montserrat:wght@400;500&family=Barlow:wght@400&display=swap">
<style>
  :root {
    --baby-blue: #86cdef;
    --ink: #1d1b1c;
    --card-black: #231f20;
    --card-white: #ffffff;
    --backdrop: #e6e4e1;
  }
  * { margin: 0; padding: 0; box-sizing: border-box; }
  html, body { width: 1200px; height: 1000px; overflow: hidden; }
  body { background: var(--backdrop); position: relative; }

  .card {
    position: absolute;
    left: 226px;
    width: 751px;
    height: 455px;
    box-shadow: 0 2px 6px rgba(0,0,0,0.25);
  }
  .card--front { top: 31px; background: var(--card-black); }
  .card--back { top: 510px; background: var(--card-white); }

  /* Front */
  .brand {
    position: absolute;
    top: 0; left: 0; right: 0; bottom: 0;
    display: flex;
    align-items: center;
    justify-content: center;
    gap: 18px;
  }
  .brand__dot {
    width: 18px; height: 18px;
    border-radius: 50%;
    background: var(--baby-blue);
  }
  .brand__name {
    font-family: "Montserrat", sans-serif;
    font-weight: 400;
    font-size: 40px;
    letter-spacing: 3px;
    color: var(--baby-blue);
  }

  /* Back: services */
  .services {
    position: absolute;
    left: 34px;
    top: 134px;
    width: 280px;
    font-family: "Bebas Neue", sans-serif;
    font-size: 29px;
    color: var(--ink);
    line-height: 1;
  }
  .services__row {
    display: flex;
    justify-content: space-between;
    height: 53px;
  }
  .service { display: flex; align-items: flex-start; gap: 3px; letter-spacing: 0.5px; }
  .service--wide { word-spacing: 6px; }
  .service__star { width: 19px; height: 19px; margin-top: 4px; fill: var(--baby-blue); }

  .divider {
    position: absolute;
    left: 338px;
    top: 137px;
    width: 2px;
    height: 188px;
    background: var(--ink);
  }

  /* Back: contact */
  .contact {
    position: absolute;
    left: 368px;
    top: 133px;
    font-family: "Barlow", sans-serif;
    color: var(--ink);
  }
  .contact__name {
    font-family: "Montserrat", sans-serif;
    font-weight: 400;
    font-size: 29px;
    letter-spacing: 1.5px;
    color: var(--baby-blue);
    margin-bottom: 34px;
    white-space: nowrap;
  }
  .contact__line {
    font-size: 23px;
    height: 44px;
    white-space: nowrap;
  }
  .contact__label { color: var(--baby-blue); margin-right: 2px; }
</style>
</head>
<body>
  <svg width="0" height="0" style="position:absolute">
    <symbol id="star" viewBox="0 0 24 24">
      <path d="M12 1.5l3.1 7 7.4.6-5.6 4.9 1.7 7.4L12 17.5l-6.6 3.9 1.7-7.4L1.5 9.1l7.4-.6z"/>
    </symbol>
  </svg>

  <section class="card card--front">
    <div class="brand">
      <span class="brand__dot"></span>
      <span class="brand__name">Harbor Kitchens</span>
    </div>
  </section>

  <section class="card card--back">
    <div class="services">
      <div class="services__row">
        <span class="service"><svg class="service__star"><use href="#star"/></svg>Kitchens</span>
        <span class="service"><svg class="service__star"><use href="#star"/></svg>Wardrobes</span>
      </div>
      <div class="services__row">
        <span class="service"><svg class="service__star"><use href="#star"/></svg>Vanities</span>
        <span class="service"><svg class="service__star"><use href="#star"/></svg>Laundries</span>
      </div>
      <div class="services__row">
        <span class="service service--wide"><svg class="service__star"><use href="#star"/></svg>Media Units</span>
        <span class="service"><svg class="service__star"><use href="#star"/></svg>Studies</span>
      </div>
      <div class="services__row">
        <span class="service service--wide"><svg class="service__star"><use href="#star"/></svg>3D Computer Designs</span>
      </div>
    </div>

    <div class="divider"></div>

    <div class="contact">
      <p class="contact__name">TED LOWTHER</p>
      <p class="contact__line"><span class="contact__label">t</span> 0491 358 902</p>
      <p class="contact__line"><span class="contact__label">e</span> harborkitchens@mailvane.example</p>
      <p class="contact__line"><span class="contact__label">ABN</span> 83 507 962 318</p>
    </div>
  </section>
</body>
</html>
```